Business Card and Stationary for Law Firm
Bellcove Law Group
Professional
Davor Tiemann
Principal Attorney
47312 Pellham Avenue, Suite 615 Cedar Hollow, California 90418
Info@theBellcoveLawGroup.example
Immigration & Nationality Law Criminal Defense ZIMR Compliance Business Entity Formation

```html
<!DOCTYPE html>
<html lang="en">
<head>
<meta charset="utf-8">
<title>Bellcove Law Group – Business Card</title>
<link rel="stylesheet" href="https://fonts.googleapis.com/css2?family=Cinzel:wght@400;700&display=swap">
<style>
  :root {
    --page-bg: #e4e6ea;
    --card-white: #ffffff;
    --card-mist: #e9ebee;
    --navy: #1d3b6e;
    --navy-deep: #132a52;
    --slate: #6d7480;
    --slate-light: #a3a9b2;
    --ink-white: #ffffff;
  }
  * { margin: 0; padding: 0; box-sizing: border-box; }
  html, body {
    width: 1200px; height: 842px; overflow: hidden;
    background: var(--page-bg);
  }
  .canvas { position: relative; width: 1200px; height: 842px; }
  .business-card {
    position: absolute; left: 60px; top: 111px;
    width: 1080px; height: 620px;
    border-radius: 40px; overflow: hidden;
    background: linear-gradient(180deg, var(--card-white) 0%, var(--card-mist) 60%);
    box-shadow: 0 10px 30px rgba(20, 30, 50, 0.18);
  }
  .card-shapes { position: absolute; inset: 0; }
  .brand {
    position: absolute; left: 220px; top: 92px;
    display: flex; align-items: center; gap: 30px;
  }
  .brand-square { width: 150px; height: 150px; background: var(--navy); }
  .brand-name {
    font-family: "Cinzel", serif; font-weight: 700;
    font-size: 46px; color: var(--navy); letter-spacing: 1px;
    white-space: nowrap;
  }
  .contact-list {
    position: absolute; left: 36px; top: 440px;
    list-style: none;
    font-family: "Cinzel", serif; font-weight: 400;
    font-size: 14.5px; line-height: 1.35; color: var(--ink-white);
  }
  .contact-list li { display: flex; align-items: flex-start; gap: 10px; margin-bottom: 5px; }
  .contact-icon { flex: 0 0 16px; width: 16px; height: 16px; margin-top: 1px; }
  .attorney {
    position: absolute; right: 46px; top: 480px; text-align: right;
    font-family: "Cinzel", serif; font-weight: 400; color: var(--ink-white);
  }
  .attorney-name { font-size: 22px; letter-spacing: 0.5px; }
  .attorney-title { font-size: 18px; margin-top: 4px; }
</style>
</head>
<body>
<main class="canvas">
  <section class="business-card">
    <svg class="card-shapes" width="1080" height="620" viewBox="0 0 1080 620" aria-hidden="true">
      <path class="swoosh-slate" d="M0,318 C260,250 520,390 780,360 C920,344 1010,290 1080,255 L1080,285 C1000,320 910,372 780,388 C520,420 260,300 0,345 Z" fill="var(--slate)"/>
      <path class="swoosh-light" d="M0,300 C280,230 540,360 800,330 C930,315 1010,270 1080,238 L1080,248 C1010,282 930,328 800,344 C540,378 280,262 0,316 Z" fill="var(--slate-light)"/>
      <path class="navy-band" d="M0,370 C260,322 520,440 780,418 C920,406 1010,350 1080,310 L1080,620 L0,620 Z" fill="var(--navy)"/>
      <path class="navy-shade" d="M0,540 C300,500 700,560 1080,470 L1080,620 L0,620 Z" fill="var(--navy-deep)" opacity="0.35"/>
    </svg>

    <div class="brand">
      <div class="brand-square"></div>
      <div class="brand-name">Bellcove Law Group</div>
    </div>

    <ul class="contact-list">
      <li>
        <svg class="contact-icon" viewBox="0 0 16 16"><circle cx="8" cy="8" r="8" fill="#fff"/><path d="M8 3.5a3 3 0 0 1 3 3c0 2.2-3 6-3 6s-3-3.8-3-6a3 3 0 0 1 3-3z" fill="var(--navy)"/></svg>
        <span>47312 Pellham Avenue, Suite 615<br>Cedar Hollow, California 90418</span>
      </li>
      <li>
        <svg class="contact-icon" viewBox="0 0 16 16"><circle cx="8" cy="8" r="8" fill="#fff"/><path d="M5 4h2l1 2.5-1.2 1a5 5 0 0 0 2.2 2.2l1-1.2L12.5 9.5v2c0 .5-.5 1-1 1A7.5 7.5 0 0 1 4 5c0-.5.5-1 1-1z" fill="var(--navy)"/></svg>
        <span>818-555-0140</span>
      </li>
      <li>
        <svg class="contact-icon" viewBox="0 0 16 16"><circle cx="8" cy="8" r="8" fill="#fff"/><rect x="4" y="5" width="8" height="6" fill="var(--navy)"/><rect x="5.5" y="3" width="5" height="2.5" fill="var(--navy)"/></svg>
        <span>818-555-0141</span>
      </li>
      <li>
        <svg class="contact-icon" viewBox="0 0 16 16"><circle cx="8" cy="8" r="8" fill="#fff"/><rect x="3.5" y="5" width="9" height="6" fill="none" stroke="var(--navy)" stroke-width="1.2"/><path d="M3.5 5l4.5 3.5 4.5-3.5" fill="none" stroke="var(--navy)" stroke-width="1.2"/></svg>
        <span>Info@theBellcoveLawGroup.example</span>
      </li>
      <li>
        <svg class="contact-icon" viewBox="0 0 16 16"><circle cx="8" cy="8" r="8" fill="#fff"/><circle cx="8" cy="8" r="4.5" fill="none" stroke="var(--navy)" stroke-width="1.1"/><path d="M3.5 8h9M8 3.5c-2 2.5-2 6.5 0 9M8 3.5c2 2.5 2 6.5 0 9" fill="none" stroke="var(--navy)" stroke-width="1"/></svg>
        <span>www.theBellcoveLawGroup.example</span>
      </li>
    </ul>

    <div class="attorney">
      <div class="attorney-name">Davor Tiemann</div>
      <div class="attorney-title">Principal Attorney</div>
    </div>
  </section>
</main>
</body>
</html>
```